Business Cards for a small business advisory (business services)

Professional look. Same as would apply for a lawyer, accountant, or other financial services professional. Please use the logo colors

Target Market(s)

small business owners

Industry/Entity Type

Financial Servics

Contact Information for Business Card

Name: Gavin L. Whitmore, CAIA / Title: Business Advisor / Office #: (718) 294-7716 / Mobile #: (917) 382-5047 / Email: g.whitmore@clearfieldventurepartners.example / Web: www.clearfieldventurepartners.example

Font styles to use
Sans Serif

```html
<!DOCTYPE html>
<html lang="en">
<head>
<meta charset="utf-8">
<title>Clearfield Venture Partners – Business Cards</title>
<link rel="stylesheet" href="https://fonts.googleapis.com/css2?family=Montserrat:wght@500;600;700&family=Arimo:wght@400;700&display=swap">
<style>
  :root {
    --navy: #1f3a6e;
    --green: #7cc242;
    --charcoal: #2e2e2f;
    --white: #ffffff;
    --ink-soft: #e9e9e9;
    --backdrop: #d9dbde;
  }
  * { box-sizing: border-box; margin: 0; padding: 0; }
  html, body {
    width: 1200px; height: 874px; overflow: hidden;
    background: var(--backdrop);
  }
  .canvas { position: relative; width: 1200px; height: 874px; }

  .card {
    position: absolute;
    width: 630px; height: 360px;
    border-radius: 26px;
    box-shadow: 0 10px 28px rgba(0,0,0,.18);
    overflow: hidden;
  }

  /* Front */
  .card--front { left: 460px; top: 70px; background: var(--white); }
  .card--front .brand {
    position: absolute; left: 0; right: 0; top: 0; bottom: 0;
    display: flex; align-items: center; justify-content: center; gap: 18px;
  }
  .brand__dot {
    width: 46px; height: 46px; border-radius: 50%;
    background: var(--green); flex: none;
  }
  .brand__name {
    font-family: "Montserrat", sans-serif; font-weight: 600;
    font-size: 38px; color: var(--navy); letter-spacing: .2px;
  }

  /* Back */
  .card--back { left: 130px; top: 450px; background: var(--charcoal); }
  .card--back .brand__name {
    position: absolute; left: 44px; top: 40px;
    font-size: 30px; color: var(--white);
  }
  .holder { position: absolute; left: 44px; top: 120px; }
  .holder__name {
    font-family: "Montserrat", sans-serif; font-weight: 700;
    font-size: 25px; color: var(--green);
  }
  .holder__title {
    font-family: "Arimo", sans-serif; font-size: 17px;
    color: var(--white); margin-top: 4px;
  }
  .contacts {
    position: absolute; left: 44px; top: 212px;
    list-style: none;
    font-family: "Arimo", sans-serif; font-size: 16px; color: var(--white);
  }
  .contacts li { display: flex; align-items: center; gap: 12px; height: 24px; }
  .contacts svg { width: 14px; height: 14px; flex: none; }

  .emblem {
    position: absolute; right: 46px; top: 96px;
    width: 168px; height: 168px; border-radius: 50%;
    border: 10px solid var(--green);
  }
</style>
</head>
<body>
<main class="canvas">

  <section class="card card--front" aria-label="Card front">
    <div class="brand">
      <span class="brand__dot"></span>
      <span class="brand__name">Clearfield Venture Partners</span>
    </div>
  </section>

  <section class="card card--back" aria-label="Card back">
    <span class="brand__name">Clearfield Venture Partners</span>

    <div class="holder">
      <p class="holder__name">Gavin L. Whitmore, CAIA</p>
      <p class="holder__title">Business Advisor</p>
    </div>

    <ul class="contacts">
      <li>
        <svg viewBox="0 0 16 16" aria-hidden="true"><path fill="var(--green)" d="M3.5 1.5l2.5 0 1 3.5-1.6 1.2a8 8 0 0 0 4.4 4.4L11 9l3.5 1v2.5c0 1-1 2-2 2A11 11 0 0 1 1.5 3.5c0-1 1-2 2-2z"/></svg>
        (718) 294-7716
      </li>
      <li>
        <svg viewBox="0 0 16 16" aria-hidden="true"><rect x="4" y="1" width="8" height="14" rx="1.5" fill="none" stroke="var(--green)" stroke-width="1.8"/><circle cx="8" cy="12.3" r="1" fill="var(--green)"/></svg>
        (917) 382-5047
      </li>
      <li>
        <svg viewBox="0 0 16 16" aria-hidden="true"><rect x="1" y="3" width="14" height="10" rx="1" fill="var(--green)"/><path d="M1.5 3.8L8 9l6.5-5.2" fill="none" stroke="var(--charcoal)" stroke-width="1.4"/></svg>
        g.whitmore@clearfieldventurepartners.example
      </li>
      <li>
        <svg viewBox="0 0 16 16" aria-hidden="true"><circle cx="8" cy="8" r="6.5" fill="none" stroke="var(--green)" stroke-width="1.6"/><path d="M1.5 8h13M8 1.5c-3 3.5-3 9.5 0 13M8 1.5c3 3.5 3 9.5 0 13" fill="none" stroke="var(--green)" stroke-width="1.2"/></svg>
        www.clearfieldventurepartners.example
      </li>
    </ul>

    <span class="emblem" aria-hidden="true"></span>
  </section>

</main>
</body>
</html>
```